Antigen Preservation Center

The company will provide a contract research services to stabilize various viruses, viral vectors, and vaccines. It may offer some licensing opportunities for stabilizing technologies. Main area of applications are pharmaceutical, therapeutic, and vaccination field. The company aspires to develop room temperature vaccines for global distribution beyond the current cold chain.
Updates

Target Market(s)

pharmaceutical, therapeutic and vaccination fields

Coding

Number of Pages Required

4 page

Requirements
Must have
• Incorporate a APC logo, attached at the bottom, on the Web page

```html
<!DOCTYPE html>
<html lang="en">
<head>
<meta charset="utf-8">
<title>Antigen Preservation Center</title>
<link rel="stylesheet" href="https://fonts.googleapis.com/css2?family=Open+Sans:wght@400;600;700;800&display=swap">
<style>
:root{
  --board:#717276;
  --gold:#b8892e;
  --green:#3f8a6a;
  --ink:#2b2b2b;
  --grey:#5c5c5c;
  --soft:#f3f1f3;
  --navy:#0d2236;
  --teal:#15505c;
  --footer:#1b1c1e;
  --white:#ffffff;
}
*{box-sizing:border-box;margin:0;padding:0}
html,body{width:1200px;height:3782px;overflow:hidden}
body{background:var(--board);font-family:"Open Sans",Arial,sans-serif;color:var(--ink);position:relative}
.desktop{position:absolute;left:38px;top:30px;width:905px;height:3057px;background:var(--white)}
.mobile{position:absolute;left:965px;top:30px;width:192px;height:3712px;background:var(--white);overflow:hidden}
.sec{position:absolute;left:0;width:100%;overflow:hidden}
.btn{display:inline-block;background:var(--gold);color:var(--white);font-weight:700;text-transform:uppercase;letter-spacing:.3px}
.btn-light{background:var(--white);color:var(--navy)}
.btn-outline{background:transparent;border:2px solid var(--white);color:var(--white)}
.rule{display:block;background:var(--green);height:3px;margin:0 auto}
.brand{display:flex;align-items:center;gap:10px;color:var(--green);font-weight:700;text-transform:uppercase;letter-spacing:1.5px;line-height:1.2}
.brand-dot{border-radius:50%;background:var(--gold);flex:none}
.lorem{color:var(--grey)}
.photo{position:absolute}

/* desktop header */
.d-header{top:0;height:96px}
.d-header .brand{position:absolute;left:100px;top:20px;font-size:15px}
.d-header .brand-dot{width:38px;height:38px}
.d-call{position:absolute;left:545px;top:20px;display:flex;gap:8px;align-items:center;font-size:8px;color:var(--grey)}
.d-call b{display:block;font-size:12px;color:var(--green)}
.d-search{position:absolute;left:680px;top:22px;width:108px;height:24px;border:1px solid #ccc;font-size:8px;color:#888;padding:6px 8px}
.d-nav{position:absolute;left:440px;top:73px;display:flex;gap:18px;font-size:9px;font-weight:700;color:var(--ink)}
.d-nav .on{color:var(--gold)}
.d-hero{top:101px;height:411px}
.d-hero .photo{inset:0;background:linear-gradient(100deg,#eef0f2 0%,#d7dde2 45%,#9fb0c0 70%,#e9ecef 100%)}
.d-hero h1{position:absolute;left:180px;top:92px;font-size:34px;line-height:1.15;font-weight:800;color:#4a4a4a}
.d-hero .btn{position:absolute;left:180px;top:178px;padding:8px 14px;font-size:11px}
.dots{position:absolute;display:flex;gap:6px}
.dots i{width:6px;height:6px;border-radius:50%;background:rgba(255,255,255,.6)}
.dots i:first-child{background:var(--gold)}

/* services */
.d-services{top:512px;height:421px;background:var(--soft);text-align:center}
.d-services h2{margin-top:48px;font-size:20px;font-weight:800}
.d-services .rule{width:26px;margin-top:8px}
.svc{position:absolute;top:122px;width:210px;text-align:center}
.svc .icon{width:70px;height:70px;margin:0 auto;border-radius:50%}
.svc h3{font-size:11px;font-weight:800;margin-top:28px}
.svc p{font-size:9px;line-height:1.35;margin-top:12px}
.svc .btn{font-size:8px;padding:4px 9px;margin-top:30px}

/* banner */
.d-viruses{top:933px;height:373px}
.d-viruses .photo{inset:0;background:radial-gradient(circle at 72% 45%,#3d6b86 0%,#183a58 35%,#0c2440 70%),#0c2440}
.d-viruses h2{position:absolute;left:143px;top:95px;font-size:31px;font-weight:800;color:var(--white)}
.d-viruses p{position:absolute;left:143px;top:140px;width:325px;font-size:13px;font-weight:600;line-height:1.3;color:var(--white)}
.d-viruses .btn{position:absolute;left:143px;top:238px;padding:7px 14px;font-size:10px}

/* welcome */
.d-welcome{top:1306px;height:383px}
.hex{position:absolute;clip-path:polygon(50% 0,100% 25%,100% 75%,50% 100%,0 75%,0 25%);background:linear-gradient(160deg,#cfe3f5,#3f7fc1 55%,#153f7a)}
.d-welcome .hex{left:100px;top:45px;width:185px;height:215px}
.welcome-text{position:absolute;left:478px;top:48px;width:330px}
.welcome-text .pre{font-size:12px;font-weight:600}
.welcome-text h2{font-size:21px;font-weight:800;line-height:1.2;margin-top:2px}
.welcome-text .rule{width:26px;margin:12px 0 14px}
.welcome-text p{font-size:9.5px;line-height:1.35}
.welcome-text .btn{font-size:10px;padding:7px 13px;margin-top:20px}

/* pick */
.d-pick{top:1689px;height:413px}
.d-pick .photo{inset:0;background:radial-gradient(circle at 75% 50%,#4f8a92 0%,#1d5a66 35%,#0e3540 75%),#0e3540}
.d-pick h2{position:absolute;left:165px;top:140px;font-size:21px;font-weight:800;line-height:1.15;color:var(--white)}
.d-pick p{position:absolute;left:165px;top:198px;width:300px;font-size:12px;line-height:1.3;color:var(--white)}
.d-pick .btn{position:absolute;left:165px;top:278px;padding:7px 14px;font-size:10px}

/* news */
.d-news{top:2102px;height:451px;background:var(--soft)}
.d-news h2{text-align:center;margin-top:50px;font-size:20px;font-weight:800}
.d-news .rule{width:26px;margin-top:8px}
.card{position:absolute;background:var(--white);border:4px solid var(--green)}
.d-news .card{width:180px;height:200px;padding:16px 18px}
.card h3{font-size:12px;font-weight:800;line-height:1.2;text-transform:uppercase}
.card p{font-size:7.5px;line-height:1.35;margin-top:8px}
.card .btn{font-size:7px;padding:3px 8px;margin-top:10px}
.card .date{position:absolute;right:-4px;bottom:-4px;background:var(--green);color:var(--white);font-size:6.5px;padding:3px 7px}
.arrow{position:absolute;width:18px;height:22px;background:#8b8b8b;color:var(--white);font-size:11px;text-align:center;line-height:22px}

/* cta */
.d-cta{top:2553px;height:245px}
.d-cta .photo,.m-cta .photo{inset:0;background:linear-gradient(120deg,#0d2740,#15385a 55%,#0d2236)}
.d-cta h2{position:absolute;left:125px;top:60px;width:380px;font-size:20px;font-weight:800;line-height:1.2;color:var(--white)}
.d-cta p{position:absolute;left:125px;top:128px;width:360px;font-size:11px;line-height:1.3;color:var(--white)}
.d-cta .btn{position:absolute;left:530px;width:245px;height:36px;line-height:32px;text-align:center;font-size:11px}
.phone-ico{display:inline-block;vertical-align:middle;margin-right:6px}

/* footer */
.d-footer{top:2798px;height:259px;background:var(--footer);color:#d8d8d8}
.d-footer .brand{position:absolute;left:100px;top:62px;font-size:14px;color:#c9c9c9}
.d-footer .brand-dot{width:36px;height:36px}
.fcol{position:absolute;font-size:8px;line-height:1.7}
.fcol h4{font-size:8px;font-weight:800;color:var(--white);margin-bottom:8px}
.ficon{display:inline-block;width:9px;height:9px;border-radius:50%;background:var(--gold);vertical-align:middle;margin-right:6px}
.social{display:flex;align-items:center;gap:6px;margin-bottom:8px}
.social i{width:15px;height:15px;border-radius:50%;background:#2b6ea8;flex:none}
.copy{position:absolute;left:0;right:0;bottom:36px;text-align:center;font-size:7.5px}

/* mobile */
.m-header{top:0;height:91px}
.burger{position:absolute;left:7px;top:18px;width:14px}
.burger i{display:block;height:2px;background:var(--ink);margin-bottom:3px}
.m-header .brand{position:absolute;left:27px;top:10px;font-size:8px;gap:5px;letter-spacing:.6px}
.m-header .brand-dot{width:20px;height:20px}
.m-call{position:absolute;left:7px;top:60px;font-size:6px;color:var(--grey)}
.m-call b{color:var(--green);font-size:8px}
.m-hero{top:91px;height:302px}
.m-hero .photo{inset:0;background:linear-gradient(110deg,#e8ebee,#b3c0cc 55%,#dfe4e8)}
.m-hero h1{position:absolute;left:10px;top:40px;font-size:14px;font-weight:800;line-height:1.1;color:#3c3c3c}
.m-hero .btn{position:absolute;left:10px;top:80px;font-size:6px;padding:3px 7px}
.m-services{top:393px;height:887px;background:var(--soft);text-align:center}
.m-services h2{margin-top:26px;font-size:13px;font-weight:800}
.m-services .rule{width:18px;margin-top:5px}
.msvc{padding:0 16px;margin-top:30px}
.msvc .icon{width:62px;height:62px;border-radius:50%;margin:0 auto}
.msvc h3{font-size:8.5px;font-weight:800;margin-top:22px}
.msvc p{font-size:7.5px;line-height:1.35;margin-top:10px}
.msvc .btn{font-size:6px;padding:3px 8px;margin-top:14px}
.m-viruses{top:1280px;height:404px}
.m-viruses .photo{inset:0;background:radial-gradient(circle at 40% 30%,#3a7588,#0f3a4c 60%,#0a2436)}
.m-viruses h2{position:absolute;left:8px;top:190px;font-size:17px;font-weight:800;line-height:1;color:var(--white)}
.m-viruses p{position:absolute;left:8px;top:232px;width:176px;font-size:8px;font-weight:600;line-height:1.3;color:var(--white)}
.m-viruses .btn{position:absolute;left:8px;top:332px;font-size:7px;padding:4px 9px}
.m-welcome{top:1684px;height:478px}
.m-welcome .inner{position:absolute;left:9px;top:16px;width:176px}
.m-welcome .pre{font-size:7.5px;font-weight:600}
.m-welcome h2{font-size:13px;font-weight:800;line-height:1.15;margin-top:2px}
.m-welcome .rule{width:16px;margin:7px 0 9px}
.m-welcome p{font-size:8px;line-height:1.4}
.m-welcome .btn{font-size:7px;padding:4px 10px;margin-top:16px}
.m-pick{top:2162px;height:378px}
.m-pick .photo{inset:0;background:radial-gradient(circle at 60% 60%,#4b858f,#1a5461 45%,#0e3340)}
.m-pick h2{position:absolute;left:32px;top:140px;width:152px;font-size:10px;font-weight:800;line-height:1.2;color:var(--white);text-align:right}
.m-pick p{position:absolute;left:32px;top:190px;width:152px;font-size:7.5px;line-height:1.3;color:var(--white);text-align:right}
.m-pick .btn{position:absolute;left:90px;top:296px;font-size:7px;padding:5px 10px}
.m-hex{position:absolute;left:8px;top:2030px;width:176px;height:200px;z-index:2}
.m-news{top:2540px;height:315px;background:var(--soft)}
.m-news h2{margin:16px 0 0 10px;font-size:11px;font-weight:800}
.m-news .rule{width:16px;margin:6px 0 0 10px}
.m-news .card{left:11px;top:63px;width:172px;height:200px;padding:16px 18px}
.m-news .card h3{font-size:12px}
.m-news .dots{left:66px;top:290px}
.m-news .dots i{background:#b5b5b5}
.m-cta{top:2868px;height:282px}
.m-cta h2{position:absolute;left:9px;top:14px;width:175px;font-size:12px;font-weight:800;line-height:1.15;color:var(--white)}
.m-cta p{position:absolute;left:9px;top:70px;width:175px;font-size:7.5px;line-height:1.3;color:var(--white)}
.m-cta .btn{position:absolute;left:7px;width:178px;height:34px;line-height:30px;font-size:9px;padding-left:12px}
.m-footer{top:3150px;height:562px;background:var(--footer);color:#d8d8d8}
.m-footer .brand{position:absolute;left:14px;top:34px;font-size:8px;gap:6px;color:#c9c9c9;letter-spacing:.8px}
.m-footer .brand-dot{width:20px;height:20px}
.m-footer .fcol{left:14px;font-size:6.5px}
.m-footer .fcol h4{font-size:6.5px;margin-bottom:5px}
.m-footer .copy{bottom:16px;font-size:6px}
</style>
</head>
<body>

<main class="desktop">
  <header class="sec d-header">
    <div class="brand"><span class="brand-dot"></span><span>Antigen<br>Preservation<br>Center</span></div>
    <div class="d-call">
      <svg width="18" height="18" viewBox="0 0 24 24"><circle cx="12" cy="12" r="11" fill="none" stroke="#3f8a6a" stroke-width="1.5"/><path d="M8 6.5l2 0 1 3-1.5 1a7 7 0 0 0 3 3l1-1.5 3 1v2a1.5 1.5 0 0 1-1.5 1.5A9 9 0 0 1 6.5 8 1.5 1.5 0 0 1 8 6.5z" fill="#3f8a6a"/></svg>
      <div>CALL US<b>888.888.8888</b></div>
    </div>
    <div class="d-search">SEARCH</div>
    <nav class="d-nav"><span class="on">HOME</span><span>ABOUT US</span><span>SERVICES</span><span>BLOG</span><span>CAREERS</span><span>CONTACT US</span></nav>
  </header>

  <section class="sec d-hero">
    <div class="photo" role="img" aria-label="Scientist in a lab coat working at a microscope in a bright laboratory"></div>
    <h1>PHARMACEUTICAL<br>RESEARCH</h1>
    <span class="btn">Read More</span>
    <div class="dots" style="left:425px;top:380px"><i></i><i></i><i></i><i></i></div>
  </section>

  <section class="sec d-services">
    <h2>OUR SERVICES</h2><span class="rule"></span>
    <div class="svc" style="left:89px">
      <div class="icon" role="img" aria-label="Green virus illustration" style="background:radial-gradient(circle,#6aa98a 30%,#e6efe9 72%)"></div>
      <h3>VARIOUS VIRUSES</h3>
      <p class="lorem">Lorem ipsum dolor sit amet consectetur adipiscing elit, sed do eiusmod tempor incididunt ut labore et dolore magna aliqua ut enim minim veniam quis nostrud.</p>
      <span class="btn">Read More</span>
    </div>
    <div class="svc" style="left:346px">
      <div class="icon" role="img" aria-label="Green viral vector illustration" style="background:radial-gradient(circle,#6aa98a 30%,#e6efe9 72%)"></div>
      <h3>VIRAL VECTORS</h3>
      <p class="lorem">Lorem ipsum dolor sit amet consectetur adipiscing elit, sed do eiusmod tempor incididunt ut labore et dolore magna aliqua ut enim minim veniam quis nostrud.</p>
      <span class="btn">Read More</span>
    </div>
    <div class="svc" style="left:598px">
      <div class="icon" role="img" aria-label="Syringe illustration on a beige circle" style="background:radial-gradient(circle,#c9a66b 25%,#efe3cf 70%)"></div>
      <h3>VACCINES</h3>
      <p class="lorem">Lorem ipsum dolor sit amet consectetur adipiscing elit, sed do eiusmod tempor incididunt ut labore et dolore magna aliqua ut enim minim veniam quis nostrud.</p>
      <span class="btn">Read More</span>
    </div>
  </section>

  <section class="sec d-viruses">
    <div class="photo" role="img" aria-label="Blue microscopic view of virus particles"></div>
    <h2>VARIOUS VIRUSES</h2>
    <p>Lorem ipsum dolor sit amet, consectetur adipiscing elit, sed do eiusmod tempor incididunt ut labore et dolore magna aliqua enim ad minim veniam.</p>
    <span class="btn btn-light">Read More</span>
  </section>

  <section class="sec d-welcome">
    <div class="hex" role="img" aria-label="Glass laboratory flask and test tube in blue light"></div>
    <div class="welcome-text">
      <div class="pre">WELCOME TO</div>
      <h2>ANTIGEN PRESERVATION<br>CENTER.</h2>
      <span class="rule"></span>
      <p class="lorem">At vero eos et accusamus et iusto odio dignissimos ducimus qui blanditiis praesentium voluptatum deleniti atque corrupti quos dolores et quas molestias excepturi sint occaecati cupiditate non provident, similique sunt in culpa qui officia deserunt mollitia animi, id est laborum et dolorum fuga. Et harum quidem rerum facilis est et expedita distinctio. Nam libero tempore, cum soluta nobis.</p>
      <span class="btn">Read More</span>
    </div>
  </section>

  <section class="sec d-pick">
    <div class="photo" role="img" aria-label="Teal microscopic view of several virus particles"></div>
    <h2>PICK THE RIGHT RESOURCES<br>FOR YOUR SPECIFIC TRAIL NEEDS</h2>
    <p>At vero eos et accusamus et iusto odio dignissimos ducimus qui blanditiis praesentium voluptatum deleniti atque corrupti quos dolores</p>
    <span class="btn">Read More</span>
  </section>

  <section class="sec d-news">
    <h2>NEWS &amp; INSIGHTS</h2><span class="rule"></span>
    <div class="arrow" style="left:0;top:238px">&#8249;</div>
    <div class="arrow" style="right:0;top:265px">&#8250;</div>
    <article class="card" style="left:55px;top:152px"><h3>At vero eos et mus et iusto odio.</h3><p class="lorem">At vero eos et accusamus et iusto odio dignissimos ducimus qui blanditiis praesentium voluptatum deleniti atque corrupti.</p><span class="btn">Read More</span><span class="date">15 JUN, 2019</span></article>
    <article class="card" style="left:262px;top:178px"><h3>At vero eos et mus et iusto odio.</h3><p class="lorem">At vero eos et accusamus et iusto odio dignissimos ducimus qui blanditiis praesentium voluptatum deleniti atque corrupti.</p><span class="btn">Read More</span><span class="date">15 JUN, 2019</span></article>
    <article class="card" style="left:466px;top:152px"><h3>At vero eos et mus et iusto odio.</h3><p class="lorem">At vero eos et accusamus et iusto odio dignissimos ducimus qui blanditiis praesentium voluptatum deleniti atque corrupti.</p><span class="btn">Read More</span><span class="date">15 JUN, 2019</span></article>
    <article class="card" style="left:673px;top:178px"><h3>At vero eos et mus et iusto odio.</h3><p class="lorem">At vero eos et accusamus et iusto odio dignissimos ducimus qui blanditiis praesentium voluptatum deleniti atque corrupti.</p><span class="btn">Read More</span><span class="date">15 JUN, 2019</span></article>
  </section>

  <section class="sec d-cta">
    <div class="photo" role="img" aria-label="Dark blue background of microscopic cells"></div>
    <h2>Lorem ipsum dolor sit amet consectetur adipiscing.</h2>
    <p>At vero eos et accusamus et iusto odio dignissimos ducimus qui blanditiis praesentium voluptatum deleniti atque corrupti quos dolores</p>
    <span class="btn" style="top:57px">Contact Us Now</span>
    <span class="btn btn-outline" style="top:104px;text-transform:none;font-weight:600"><svg class="phone-ico" width="10" height="10" viewBox="0 0 24 24"><path d="M5 2h4l2 5-2.5 1.5a11 11 0 0 0 7 7L17 13l5 2v4a2 2 0 0 1-2 2A18 18 0 0 1 3 4a2 2 0 0 1 2-2z" fill="#fff"/></svg>Call us on 888.888.8888</span>
  </section>

  <footer class="sec d-footer">
    <div class="brand"><span class="brand-dot"></span><span>Antigen<br>Preservation<br>Center</span></div>
    <div class="fcol" style="left:400px;top:40px">
      <h4>CONTACT US</h4>
      <div><span class="ficon"></span>Lindenweg 24</div>
      <div style="padding-left:15px;margin-top:-3px">4811 AB Ravensburg, The Netherlands</div>
      <div style="margin-top:6px"><span class="ficon"></span>888.888.8888</div>
      <div style="margin-top:6px"><span class="ficon"></span>info@antigenpreservation.example</div>
    </div>
    <div class="fcol" style="left:615px;top:40px">
      <h4>MENU</h4>
      <div>HOME</div><div>ABOUT US</div><div>SERVICES</div><div>BLOG</div><div>CAREERS</div><div>CONTACT US</div>
    </div>
    <div class="fcol" style="left:715px;top:40px">
      <h4>CONNECT WITH US</h4>
      <div class="social"><i></i>Community</div>
      <div class="social"><i style="background:#3d9bd6"></i>Updates</div>
      <div class="social"><i style="background:#2a6496"></i>Network</div>
    </div>
    <div class="copy">Copyrights @ 2019 All Rights Reserved</div>
  </footer>
</main>

<main class="mobile">
  <header class="sec m-header">
    <div class="burger"><i></i><i></i><i></i></div>
    <div class="brand"><span class="brand-dot"></span><span>Antigen<br>Preservation<br>Center</span></div>
    <div class="m-call">CALL US <b>888.888.8888</b></div>
  </header>

  <section class="sec m-hero">
    <div class="photo" role="img" aria-label="Scientist at a microscope in a laboratory"></div>
    <h1>PHARMACEUTICAL<br>RESEARCH</h1>
    <span class="btn">Read More</span>
    <div class="dots" style="left:72px;top:285px"><i></i><i></i><i></i><i></i></div>
  </section>

  <section class="sec m-services">
    <h2>OUR SERVICES</h2><span class="rule"></span>
    <div class="msvc">
      <div class="icon" role="img" aria-label="Green virus illustration" style="background:radial-gradient(circle,#6aa98a 30%,#e6efe9 72%)"></div>
      <h3>VARIOUS VIRUSES</h3>
      <p class="lorem">Lorem ipsum dolor sit amet consectetur adipiscing elit, sed do eiusmod tempor incididunt ut labore et dolore magna aliqua ut enim minim veniam quis nostrud.</p>
      <span class="btn">Read More</span>
    </div>
    <div class="msvc" style="margin-top:50px">
      <div class="icon" role="img" aria-label="Green viral vector illustration" style="background:radial-gradient(circle,#6aa98a 30%,#e6efe9 72%)"></div>
      <h3>VIRAL VECTORS</h3>
      <p class="lorem">Lorem ipsum dolor sit amet consectetur adipiscing elit, sed do eiusmod tempor incididunt ut labore et dolore magna aliqua ut enim minim veniam quis nostrud.</p>
      <span class="btn">Read More</span>
    </div>
    <div class="msvc" style="margin-top:50px">
      <div class="icon" role="img" aria-label="Syringe illustration on a beige circle" style="background:radial-gradient(circle,#c9a66b 25%,#efe3cf 70%)"></div>
      <h3>VACCINES</h3>
      <p class="lorem">Lorem ipsum dolor sit amet consectetur adipiscing elit, sed do eiusmod tempor incididunt ut labore et dolore magna aliqua ut enim minim veniam quis nostrud.</p>
      <span class="btn">Read More</span>
    </div>
  </section>

  <section class="sec m-viruses">
    <div class="photo" role="img" aria-label="Blue microscopic view of virus particles"></div>
    <h2>VARIOUS<br>VIRUSES</h2>
    <p>Lorem ipsum dolor sit amet, consectetur adipiscing elit, sed do eiusmod tempor incididunt ut labore et dolore magna aliqua enim ad minim veniam.</p>
    <span class="btn btn-light">Read More</span>
  </section>

  <section class="sec m-welcome">
    <div class="inner">
      <div class="pre">WELCOME TO</div>
      <h2>ANTIGEN<br>PRESERVATION<br>CENTER.</h2>
      <span class="rule"></span>
      <p class="lorem">At vero eos et accusamus et iusto odio dignissimos ducimus qui blanditiis praesentium voluptatum deleniti atque corrupti quos dolores et quas molestias excepturi sint occaecati cupiditate non provident, similique sunt in culpa qui officia deserunt mollitia animi, id est laborum et dolorum fuga. Et harum quidem rerum facilis est et expedita distinctio. Nam libero tempore, cum soluta nobis.</p>
      <span class="btn">Read More</span>
    </div>
  </section>

  <section class="sec m-pick">
    <div class="photo" role="img" aria-label="Teal microscopic view of virus particles"></div>
    <h2>PICK THE RIGHT RESOURCES FOR YOUR SPECIFIC TRAIL NEEDS</h2>
    <p>At vero eos et accusamus et iusto odio dignissimos ducimus qui blanditiis praesentium voluptatum deleniti atque corrupti quos dolores</p>
    <span class="btn">Read More</span>
  </section>

  <div class="hex m-hex" role="img" aria-label="Glass laboratory flask in blue light"></div>

  <section class="sec m-news">
    <h2>NEWS &amp; INSIGHTS</h2><span class="rule"></span>
    <article class="card"><h3>At vero eos et mus et iusto odio.</h3><p class="lorem">At vero eos et accusamus et iusto odio dignissimos ducimus qui blanditiis praesentium voluptatum deleniti atque corrupti.</p><span class="btn">Read More</span><span class="date">15 JUN, 2019</span></article>
    <div class="dots"><i></i><i></i><i></i><i></i><i></i></div>
  </section>

  <section class="sec m-cta">
    <div class="photo" role="img" aria-label="Dark blue background of microscopic cells"></div>
    <h2>Lorem ipsum dolor sit amet consectetur adipiscing.</h2>
    <p>At vero eos et accusamus et iusto odio dignissimos ducimus qui blanditiis praesentium voluptatum deleniti atque corrupti quos dolores</p>
    <span class="btn" style="top:160px">Contact Us Now</span>
    <span class="btn btn-outline" style="top:212px;text-transform:none;font-weight:600"><svg class="phone-ico" width="9" height="9" viewBox="0 0 24 24"><path d="M5 2h4l2 5-2.5 1.5a11 11 0 0 0 7 7L17 13l5 2v4a2 2 0 0 1-2 2A18 18 0 0 1 3 4a2 2 0 0 1 2-2z" fill="#fff"/></svg>Call us on 888.888.8888</span>
  </section>

  <footer class="sec m-footer">
    <div class="brand"><span class="brand-dot"></span><span>Antigen<br>Preservation<br>Center</span></div>
    <div class="fcol" style="top:100px">
      <h4>CONTACT US</h4>
      <div><span class="ficon"></span>Lindenweg 24</div>
      <div style="padding-left:15px">4811 AB Ravensburg, The Netherlands</div>
      <div style="margin-top:6px"><span class="ficon"></span>888.888.8888</div>
      <div style="margin-top:6px"><span class="ficon"></span>info@antigenpreservation.example</div>
    </div>
    <div class="fcol" style="top:240px">
      <h4>MENU</h4>
      <div>HOME</div><div>ABOUT US</div><div>SERVICES</div><div>BLOG</div><div>CAREERS</div><div>CONTACT US</div>
    </div>
    <div class="fcol" style="top:380px">
      <h4>CONNECT WITH US</h4>
      <div class="social"><i></i>Community</div>
      <div class="social"><i style="background:#3d9bd6"></i>Updates</div>
      <div class="social"><i style="background:#2a6496"></i>Network</div>
    </div>
    <div class="copy">Copyrights @ 2019 All Rights Reserved</div>
  </footer>
</main>

</body>
</html>
```